Vel-Trax.ch is looking for business card letterhead and envelope C5 with WOW effect

We need a strong business card for our company Vel-Trax.ch, logo is available. You want a black or dark background on which the logo Stark r% 26 # 252; appears. Letterhead and envelope in C5 format should be in a similar design, but does not have to be We need a strong business card for our company Vel-Trax.ch, logo is available. A black or dark background is desired, on which the logo Stark comes across. The letterhead and the envelope in C5 format should have a similar design.

Target Market(s)

Private customers as well as entrepreneurs

Contact Information for Business Card

E-mail: info@vel-trax.ch
Web.www.Vel-Trax.ch
Tel: +41 ( 0 ) 79 684 3027
Adresse:
Lindenhaldeweg 14
9403 Brenzikon

Hier kann man Icons verwenden für Email,Tel und Adressse

Font styles to use
Other font styles liked:
• Dubai,bold

Colors

Designer to choose colors to be used in the design.

Requirements
Must have
• WOW effect
Nice to have
• R% 26 # 252; back business card with our service listings. - VEHICLE LABELING - SHOP WINDOW LABELING - STICKERS AND MUCH MORE ... in red color

```html
<!DOCTYPE html>
<html lang="de">
<head>
<meta charset="utf-8">
<title>Vel-Trax.ch – Geschäftsausstattung</title>
<link rel="stylesheet" href="https://fonts.googleapis.com/css2?family=Open+Sans:wght@400;600;700&display=swap">
<style>
  :root {
    --ink: #070808;
    --ink-flap: #0b0c0c;
    --yellow: #f1c419;
    --yellow-faint: #f4ebd2;
    --red: #d0202a;
    --paper: #f5f5f5;
    --white: #ffffff;
    --window: #d4d4d6;
    --stage: #e3e3e5;
    --stage-light: #ececed;
  }
  * { margin: 0; padding: 0; box-sizing: border-box; }
  html, body { width: 1200px; height: 991px; overflow: hidden; }
  body {
    position: relative;
    background: radial-gradient(ellipse at 50% 50%, var(--stage-light) 0%, var(--stage) 70%);
    font-family: "Open Sans", Arial, sans-serif;
    color: var(--white);
  }
  .piece { position: absolute; box-shadow: 1px 2px 4px rgba(0,0,0,.35); overflow: hidden; }
  .wordmark {
    position: absolute;
    font-weight: 700;
    letter-spacing: .02em;
    color: var(--white);
    white-space: nowrap;
    display: flex; align-items: center;
  }
  .wordmark .dot { display: inline-block; background: var(--yellow); margin-right: .4em; }

  /* Business card front */
  .card-front { left: 93px; top: 72px; width: 196px; height: 127px; background: var(--ink); }
  .card-front .wordmark { right: 15px; top: 54px; font-size: 12.5px; }
  .card-front .wordmark .dot { width: 8px; height: 8px; }
  .services {
    position: absolute; right: 15px; top: 86px;
    list-style: none; text-align: right;
    font-size: 4.8px; line-height: 8px; color: var(--red); text-transform: uppercase;
  }

  /* Business card back */
  .card-back { left: 318px; top: 72px; width: 196px; height: 127px; background: var(--ink); }
  .card-back .wordmark { left: 16px; top: 55px; font-size: 8px; }
  .card-back .wordmark .dot { width: 6px; height: 6px; }
  .card-back .rule { position: absolute; left: 109px; top: 32px; width: 1px; height: 62px; background: var(--yellow); }
  .card-back .contact { position: absolute; left: 118px; top: 32px; font-size: 4.6px; line-height: 7px; }
  .card-back .person { color: var(--yellow); font-size: 6.8px; font-weight: 600; line-height: 8px; }
  .card-back .role { margin-bottom: 8px; }
  .card-back .address { margin-bottom: 3px; }
  .contact-row { display: flex; align-items: center; gap: 3px; }
  .contact-row svg { fill: var(--yellow); flex: none; }

  /* Letterhead */
  .letterhead { left: 74px; top: 233px; width: 483px; height: 683px; background: var(--paper); }
  .letterhead .header { position: absolute; left: 0; top: 0; }
  .letterhead .wordmark { left: 40px; top: 29px; font-size: 13.5px; }
  .letterhead .wordmark .dot { width: 9px; height: 9px; }
  .letterhead .rule { position: absolute; left: 359px; top: 11px; width: 1px; height: 42px; background: var(--yellow); }
  .letterhead .contact { position: absolute; left: 377px; top: 12px; font-size: 7.4px; line-height: 10px; }
  .letterhead .contact-row svg { width: 7px; height: 7px; margin-right: 2px; }
  .letterhead .backdrop-pattern {
    position: absolute; left: 279px; top: 431px; width: 204px; height: 252px;
    background: linear-gradient(140deg, rgba(244,235,210,0) 15%, var(--yellow-faint) 60%);
  }
  .letterhead .site { position: absolute; left: 209px; top: 650px; font-size: 7.6px; letter-spacing: .08em; color: #222; }

  /* Envelope front */
  .envelope-front { left: 602px; top: 79px; width: 527px; height: 373px; background: var(--ink); }
  .envelope-front .wordmark { left: 51px; top: 47px; font-size: 16px; }
  .envelope-front .wordmark .dot { width: 11px; height: 11px; }
  .envelope-front .sender { position: absolute; left: 51px; top: 115px; font-size: 7.8px; letter-spacing: .1em; }
  .envelope-front .window {
    position: absolute; left: 51px; top: 138px; width: 218px; height: 87px;
    border-radius: 6px; background: var(--window); box-shadow: inset 0 0 2px rgba(0,0,0,.35);
  }
  .envelope-front .backdrop-pattern {
    position: absolute; left: 319px; top: 117px; width: 208px; height: 256px;
    background: linear-gradient(140deg, rgba(241,196,25,0) 10%, rgba(241,196,25,.55) 45%, var(--yellow) 80%);
  }

  /* Envelope back */
  .envelope-back { left: 602px; top: 535px; width: 527px; height: 372px; background: var(--ink); }
  .envelope-back .flap {
    position: absolute; left: 4px; top: 0; width: 519px; height: 86px;
    background: var(--ink-flap); border-radius: 0 0 12px 12px;
    box-shadow: 0 3px 5px rgba(0,0,0,.6);
  }
  .envelope-back .wordmark { left: 0; right: 0; top: 32px; justify-content: center; font-size: 15px; }
  .envelope-back .wordmark .dot { width: 10px; height: 10px; }
</style>
</head>
<body>

<section class="piece card-front" aria-label="Visitenkarte Vorderseite">
  <div class="wordmark"><span class="dot"></span>VEL-TRAX.CH</div>
  <ul class="services">
    <li>Vehicle labeling</li>
    <li>Shop window labeling</li>
    <li>Stickers and much more</li>
  </ul>
</section>

<section class="piece card-back" aria-label="Visitenkarte Rückseite">
  <div class="wordmark"><span class="dot"></span>VEL-TRAX.CH</div>
  <div class="rule"></div>
  <div class="contact">
    <p class="person">Daniel Brunner</p>
    <p class="role">President</p>
    <p>Lindenhaldeweg 14</p>
    <p class="address">9418 Brenzikon</p>
    <p class="contact-row"><svg width="4" height="4" viewBox="0 0 10 10"><path d="M2 0l2 2.5-1.2 1.3a6 6 0 0 0 3.4 3.4L7.5 6 10 8l-1.5 2C4 10 0 6 0 1.5z"/></svg>+41 ( 0 ) 79 684 3027</p>
    <p class="contact-row"><svg width="4" height="4" viewBox="0 0 10 10"><path d="M0 1.5h10v7H0zM1 2.5l4 3 4-3v-.2H1z" fill-rule="evenodd"/></svg>info@vel-trax.ch</p>
    <p class="contact-row"><svg width="4" height="4" viewBox="0 0 10 10"><circle cx="5" cy="5" r="4.5" fill="none" stroke="#f1c419" stroke-width="1.2"/><path d="M.5 5h9M5 .5c-2.5 3-2.5 6 0 9M5 .5c2.5 3 2.5 6 0 9" fill="none" stroke="#f1c419" stroke-width=".8"/></svg>www.Vel-Trax.ch</p>
  </div>
</section>

<section class="piece letterhead" aria-label="Briefpapier">
  <svg class="header" width="483" height="82" viewBox="0 0 483 82"><path d="M0 0H483V61H180L160 82H0Z" fill="var(--ink)"/></svg>
  <div class="wordmark"><span class="dot"></span>VEL-TRAX.CH</div>
  <div class="rule"></div>
  <div class="contact">
    <p>Lindenhaldeweg 14</p>
    <p>9418 Brenzikon</p>
    <p class="contact-row"><svg viewBox="0 0 10 10"><path d="M2 0l2 2.5-1.2 1.3a6 6 0 0 0 3.4 3.4L7.5 6 10 8l-1.5 2C4 10 0 6 0 1.5z"/></svg>+41 ( 0 ) 79 684 3027</p>
    <p class="contact-row"><svg viewBox="0 0 10 10"><path d="M0 1.5h10v7H0zM1 2.5l4 3 4-3v-.2H1z" fill-rule="evenodd"/></svg>info@vel-trax.ch</p>
  </div>
  <div class="backdrop-pattern" role="img" aria-label="Faint honeycomb decoration in the lower right corner"></div>
  <p class="site">www.Vel-Trax.ch</p>
</section>

<section class="piece envelope-front" aria-label="Couvert C5 Vorderseite">
  <div class="wordmark"><span class="dot"></span>VEL-TRAX.CH</div>
  <p class="sender">Lindenhaldeweg 14 • 9418 Brenzikon</p>
  <div class="window"></div>
  <div class="backdrop-pattern" role="img" aria-label="Yellow honeycomb decoration in the lower right corner"></div>
</section>

<section class="piece envelope-back" aria-label="Couvert C5 Rückseite">
  <div class="flap"></div>
  <div class="wordmark"><span class="dot"></span>VEL-TRAX.CH</div>
</section>

</body>
</html>
```